Design for Certificate

Design a certificate for training, providing our company logo such as attachments. Company's name is "ØSTRA Velmark Advisory Ltd", please refer to our company profile: https://www.ostra-velmark.example/company_info

The style of the current certificate is also attached, and another certificate of another company can be referred to. Psd & jpg are required for the final draft (the layers of psd are not merged). Thanks!

```html
<!DOCTYPE html>
<html lang="en">
<head>
<meta charset="utf-8">
<title>ØSTRA Velmark Advisory Ltd — Certificate of Completion</title>
<link rel="stylesheet" href="https://fonts.googleapis.com/css2?family=Tinos:wght@400;700&display=swap">
<style>
  :root {
    --backdrop: #a9a9a9;
    --paper: #ffffff;
    --ink: #111111;
    --accent: #e6bb98;
    --rule: #555555;
    --trim: #8a8a8a;
    --wave-tone: #ececec;
  }
  * { margin: 0; padding: 0; box-sizing: border-box; }
  html, body {
    width: 1200px; height: 917px; overflow: hidden;
    background: var(--backdrop);
    font-family: "Tinos", "Times New Roman", serif;
    color: var(--ink);
  }
  .certificate {
    position: absolute; left: 283px; top: 52px;
    width: 573px; height: 808px;
    background: var(--paper);
    overflow: hidden;
  }
  .trim-lines { position: absolute; inset: 0; }
  .wave-field {
    position: absolute; left: 0; right: 0; top: 418px; bottom: 0;
    background: linear-gradient(170deg, rgba(255,255,255,0) 0%, var(--wave-tone) 45%, #f3f3f3 75%, rgba(255,255,255,0) 100%);
    opacity: .8;
  }
  .centered { position: absolute; left: 0; width: 100%; text-align: center; }
  .cert-number {
    position: absolute; left: 364px; top: 41px;
    font-size: 11.5px; display: flex; align-items: flex-end; gap: 5px;
  }
  .cert-number .blank { display: inline-block; width: 85px; border-bottom: 1px solid var(--rule); height: 10px; }
  .brand-name {
    top: 78px; font-size: 92px; line-height: 1; color: var(--accent);
    letter-spacing: 2px;
  }
  .title {
    top: 198px; font-size: 29px; font-weight: 700; color: var(--accent);
    letter-spacing: .3px;
  }
  .awarded { top: 282px; font-size: 17px; letter-spacing: .2px; }
  .recipient-line {
    position: absolute; left: 99px; top: 362px; width: 373px;
    border-top: 1px solid var(--rule);
  }
  .completed { top: 373px; font-size: 15px; }
  .course {
    top: 448px; font-size: 24px; line-height: 34px; font-weight: 700;
    color: var(--accent);
  }
  .duration {
    position: absolute; left: 139px; top: 575px; font-size: 15px;
    display: flex; align-items: flex-end; gap: 12px;
  }
  .duration .blank { display: inline-block; width: 139px; border-bottom: 1px solid var(--rule); height: 14px; }
  .issuer {
    position: absolute; left: 38px; top: 704px;
    font-size: 28px; font-weight: 700; white-space: nowrap;
  }
  .seal { position: absolute; left: 244px; top: 643px; width: 83px; height: 134px; }
  .signature-line {
    position: absolute; left: 353px; top: 722px; width: 176px;
    border-top: 1px solid var(--rule);
  }
  .signatory { position: absolute; left: 358px; top: 731px; font-size: 11px; letter-spacing: .2px; }
</style>
</head>
<body>
  <main class="certificate">
    <div class="wave-field" role="img" aria-label="Faint flowing wavy line pattern across the lower half of the certificate"></div>

    <svg class="trim-lines" width="573" height="808" aria-hidden="true">
      <g stroke="var(--trim)" stroke-width="1" stroke-dasharray="2 2" fill="none">
        <line x1="16" y1="0" x2="16" y2="808"/>
        <line x1="20" y1="0" x2="20" y2="808"/>
        <line x1="555" y1="0" x2="555" y2="808"/>
        <line x1="559" y1="0" x2="559" y2="808"/>
        <line x1="0" y1="17" x2="573" y2="17"/>
        <line x1="0" y1="21" x2="573" y2="21"/>
        <line x1="0" y1="788" x2="573" y2="788"/>
        <line x1="0" y1="792" x2="573" y2="792"/>
      </g>
    </svg>

    <div class="cert-number">Certificate NO: <span class="blank"></span></div>

    <div class="centered brand-name">ØSTRA</div>

    <h1 class="centered title">CERTIFICATE OF COMPLETION</h1>
    <p class="centered awarded">THIS CERTIFICATE IS AWARDED TO</p>
    <div class="recipient-line"></div>
    <p class="centered completed">has successfully completed</p>

    <h2 class="centered course">BRAND REPUTATION MANAGEMENT<br>TRAINING COURSE</h2>

    <p class="duration">Sxteen hours, hold on <span class="blank"></span></p>

    <p class="issuer">ØSTRA Velmark</p>

    <svg class="seal" viewBox="0 0 83 134" aria-hidden="true">
      <rect x="1" y="1" width="81" height="132" fill="none" stroke="var(--accent)" stroke-width="1.5"/>
    </svg>

    <div class="signature-line"></div>
    <p class="signatory">CHIEF TECHNOLOGY OFFICER</p>
  </main>
</body>
</html>
```